Book Cover Design Project - Lesbian stories

I need a cover for my ebook of short stories. Target market is lesbians. I want something erotic (but not too over the top or porny). Something tasteful and feminine. For example two women with a flower see artist Mirel Dunstan http://www.galvoristudio.example/magazine/article.php?articleID=287.

Title: Harbour Letters, Paper Moons

By Lucinda Marvaro

```html
<!DOCTYPE html>
<html lang="en">
<head>
<meta charset="utf-8">
<title>Harbour Letters, Paper Moons — Lucinda Marvaro</title>
<link rel="stylesheet" href="https://fonts.googleapis.com/css2?family=Montserrat:wght@500;800&family=Sue+Ellen+Francisco&display=swap">
<style>
  :root {
    --page: #ffffff;
    --ink: #000000;
    --crimson: #c8161a;
    --crimson-deep: #a80f12;
    --saffron: #efa520;
    --title: #ffffff;
  }
  html, body {
    margin: 0;
    padding: 0;
    width: 900px;
    height: 1200px;
    overflow: hidden;
    background: var(--page);
  }
  .canvas {
    position: relative;
    width: 900px;
    height: 1200px;
    background: var(--page);
  }
  .cover {
    position: absolute;
    left: 111px;
    top: 78px;
    width: 669px;
    height: 1064px;
    background: var(--ink);
    overflow: hidden;
  }
  .cover-art {
    position: absolute;
    inset: 0;
    background:
      radial-gradient(ellipse 260px 230px at 74% 30%, var(--saffron) 0%, rgba(239,165,32,0.85) 45%, rgba(239,165,32,0) 100%),
      radial-gradient(ellipse 330px 560px at 28% 48%, var(--crimson) 0%, rgba(200,22,26,0.8) 50%, rgba(200,22,26,0) 100%),
      radial-gradient(ellipse 320px 240px at 48% 77%, var(--crimson-deep) 0%, rgba(168,15,18,0.85) 50%, rgba(168,15,18,0) 100%),
      var(--ink);
  }
  .author {
    position: absolute;
    left: 413px;
    top: 282px;
    margin: 0;
    color: var(--ink);
    font-family: "Montserrat", Arial, sans-serif;
    line-height: 1;
  }
  .author-first {
    display: block;
    font-weight: 800;
    font-size: 38px;
    letter-spacing: 3px;
  }
  .author-last {
    display: block;
    margin-top: 8px;
    font-weight: 500;
    font-size: 24px;
    letter-spacing: 9px;
  }
  .title {
    position: absolute;
    left: 60px;
    width: 575px;
    top: 722px;
    margin: 0;
    text-align: center;
    color: var(--title);
    font-family: "Sue Ellen Francisco", cursive;
    font-weight: 400;
    font-size: 76px;
    line-height: 70px;
    letter-spacing: 1px;
  }
  .title span { display: block; }
</style>
</head>
<body>
  <main class="canvas">
    <article class="cover">
      <div class="cover-art" role="img" aria-label="Abstract painted illustration of two flowing figures, a red one with dark curly hair on the left and a golden one at the upper right, on black"></div>
      <p class="author">
        <span class="author-first">LUCINDA</span>
        <span class="author-last">marvaro</span>
      </p>
      <h1 class="title">
        <span>Harbour Letters,</span>
        <span>Paper Moons</span>
      </h1>
    </article>
  </main>
</body>
</html>
```